Flyer for outback tour company

Trifold flyer with a page for each tour that we offer (4 different tours) as well as a front page and a contact page.

Front page: Kestrel Treks logo + an overview of the tours on offer:
- Grand Circuit of the Village and Ridgelands
- Opalvale Showcase Tour
- Twilight Ridgelands Tour
- Subsurface Gemhunt (prospecting) Tour.

Page 2-5: description of each tour with pricing/duration.

Last page (back of brochure): contact details.
Ph: 0488 217 654
E-mail: kestreltreksoz@mailbox-example.net
Online bookings: www.kestreltreksoz-example.com.au.
Tours can also be booked directly through the reception at the Harlow Ridge Desert Lodge and the Clay Nest Inn. Please include the logos for Harlow Ridge and Clay Nest on the last page.

Target Market(s)

Travellers/tourists

Industry/Entity Type

Tourism/tour company

Font styles to use
Sans Serif

Requirements
Must have
• In regards to the pictures… the picture with the tour guide shining the torch should be on the page with the Gemhunt Tour. The other pictures of the cave tunnels should only be on the premium tour/Gemhunt Tour or front/back page.

```html
<!DOCTYPE html>
<html lang="en">
<head>
<meta charset="utf-8">
<title>Kestrel Treks – Trifold Flyer</title>
<link href="https://fonts.googleapis.com/css2?family=Poppins:wght@400;500;600;700;800&display=swap" rel="stylesheet">
<style>
  :root{
    --rust:#b5441f;
    --rust-bright:#d4552a;
    --charcoal:#2b2b2b;
    --paper:#ededed;
    --ink:#1f1f1f;
    --white:#ffffff;
    --stage:#f3f3f3;
  }
  *{box-sizing:border-box;margin:0;padding:0}
  html,body{width:1200px;height:800px;overflow:hidden;background:var(--stage)}
  body{font-family:'Poppins',sans-serif;color:var(--ink);position:relative}
  .sheet{position:absolute;top:180px;width:560px;height:420px;display:flex;box-shadow:0 12px 30px rgba(0,0,0,.18)}
  .sheet--inside{left:25px}
  .sheet--outside{left:615px}
  .panel{position:relative;width:33.333%;height:100%;overflow:hidden;font-size:8.2px;line-height:1.3}
  .panel--rust{background:var(--rust);color:var(--white);padding:22px 16px}
  .panel--light{background:var(--paper)}
  .panel--dark{background:var(--charcoal);color:var(--white)}
  .title{font-weight:800;text-transform:uppercase;font-size:11px;line-height:1.15}
  .title .accent{color:var(--rust-bright)}
  .rule{width:24px;height:3px;background:var(--rust-bright);margin:6px 0 8px}
  .panel--rust .rule{background:var(--white)}
  .center{text-align:center}
  .center .rule{margin-left:auto;margin-right:auto}
  .meta{font-weight:600;font-size:8.6px;margin-bottom:3px}
  .body{margin:5px 0}
  .subhead{font-weight:800;text-transform:uppercase;font-size:9.5px;margin-top:8px}
  .ticks{list-style:none;margin-top:2px}
  .ticks li{position:relative;padding-left:13px;margin-bottom:4px}
  .ticks li::before{content:"";position:absolute;left:0;top:1.5px;width:7px;height:7px;border:1px solid currentColor;border-radius:50%}
  .ticks li::after{content:"";position:absolute;left:2.3px;top:3.3px;width:2.5px;height:1.5px;border-left:1px solid currentColor;border-bottom:1px solid currentColor;transform:rotate(-45deg)}
  .ticks--rust li::before,.ticks--rust li::after{border-color:var(--rust-bright)}
  .photo{position:absolute;left:0;width:100%}
  .wave{position:absolute;left:0;width:100%}
  .text-block{position:absolute;left:14px;right:14px;z-index:2}
  /* highlights panel */
  .photo--canyon{top:0;height:150px;background:linear-gradient(180deg,#6f8fb8 0%,#a9bcd0 55%,#b58a5e 75%,#7a4f30 100%)}
  .photo--ridges{bottom:0;height:150px;background:linear-gradient(180deg,#2f6fb3 0%,#7fb0d8 35%,#c98a4c 60%,#8a4a22 100%)}
  .photo--tunnel{bottom:0;height:145px;background:radial-gradient(circle at 40% 40%,#a8aaa3 0%,#6d6a5f 40%,#3d342b 100%)}
  .photo--glasses{top:0;height:235px;background:linear-gradient(180deg,#7da0c6 0%,#c9a888 35%,#a7653a 60%,#4b2e20 100%)}
  /* contact */
  .contact{padding:30px 14px 0;text-align:center}
  .contact .title{font-size:15px;color:var(--ink)}
  .icon{display:block;margin:8px auto 3px}
  .contact .line{font-weight:500;font-size:8.3px}
  .booking-bar{background:var(--rust-bright);color:var(--white);font-weight:800;text-transform:uppercase;font-size:10px;padding:4px 0;margin:10px -4px 6px}
  .brand-row{display:flex;align-items:center;justify-content:center;gap:5px;margin-top:12px;font-weight:700;color:var(--rust)}
  .brand-row .mark-square{width:14px;height:14px;background:var(--rust)}
  .brand-row .mark-circle{width:14px;height:14px;border-radius:50%;background:var(--rust)}
  .brand-row--lodge{font-size:9px;margin-top:8px}
  .brand-row--inn{font-size:12px}
  .partners{display:flex;justify-content:center;gap:10px;margin-top:10px}
  .partner{width:34px;height:14px;border-radius:3px;background:#3b7fc4}
  .partner--green{background:#7bae3c}
  /* front */
  .emblem{position:absolute;left:50%;top:188px;transform:translateX(-50%);width:92px;height:92px;border-radius:50%;background:var(--paper);display:flex;flex-direction:column;align-items:center;justify-content:center;gap:4px;font-weight:800;font-size:11px;color:var(--charcoal);text-transform:uppercase}
  .emblem .mark-square{width:10px;height:10px;background:var(--rust-bright)}
  .front-list{position:absolute;left:14px;right:10px;top:295px;font-size:8.2px}
</style>
</head>
<body>

<section class="sheet sheet--inside" aria-label="Inside spread">

  <article class="panel panel--rust">
    <h2 class="title">Grand Circuit of the Village and Ridgelands</h2>
    <div class="rule"></div>
    <p class="meta">$99 adults/$75 children</p>
    <p class="meta">Duration: approx. 5 hours</p>
    <p class="meta">1pm start</p>
    <p class="meta">Complimentary sparkling wine is provided at the Ridgelands lookout</p>
    <p class="body">Smaller groups, bigger experience. Sit back and relax in our spacious air-conditioned 4wd vehicle as we take you places in and around Opalvale that the others can't.</p>
    <h3 class="subhead">The tour includes</h3>
    <div class="rule"></div>
    <ul class="ticks">
      <li>The Old Stone Underground Chapel</li>
      <li>Modern Underground Home (dugout)</li>
      <li>The Lunar Flats</li>
      <li>The Boundary Fence</li>
      <li>The Ridgelands</li>
      <li>Underground Mine Tour at our private claim in the opal fields (exclusive to Kestrel Treks)</li>
    </ul>
  </article>

  <article class="panel panel--light">
    <div class="photo photo--canyon" role="img" aria-label="Tour vehicle parked between sandstone cliffs under a blue sky"></div>
    <svg class="wave" style="top:112px" width="187" height="60" viewBox="0 0 187 60" preserveAspectRatio="none" aria-hidden="true">
      <path d="M0 30 C50 5 110 55 187 20 L187 60 L0 60 Z" fill="#2b2b2b"/>
      <path d="M0 36 C50 12 110 62 187 28 L187 60 L0 60 Z" fill="#ededed"/>
    </svg>
    <div class="text-block center" style="top:168px">
      <h2 class="title"><span class="accent">Opalvale</span><br>Showcase Tour</h2>
      <div class="rule"></div>
      <p class="meta">$85 adults/ $59 children</p>
      <p class="meta">Family rate<br>(2 adults and 2 children): $270</p>
      <p class="meta">Duration approx: 5 hours</p>
      <p class="body">A tour that gives you a great insight and introduction into this unique outback town and the surrounding area. Highlights include:</p>
      <p>Glimmerstone Opal Mine &amp; Museum</p>
      <p style="margin-bottom:5px">The Old Stone Underground Chapel</p>
      <ul class="ticks ticks--rust" style="display:inline-block;text-align:left">
        <li>The boundary fence</li>
        <li>The Lunar Flats</li>
        <li>The Ridgelands</li>
      </ul>
    </div>
  </article>

  <article class="panel panel--light" style="background:var(--white)">
    <div class="text-block" style="top:22px">
      <h2 class="title"><span class="accent">Twilight Ridgelands</span><br>Tour: $60</h2>
      <div class="rule"></div>
      <p class="meta">Duration approx. 3.5 hours</p>
      <p class="meta">Departs 3 hours before sunset</p>
      <p class="body">A perfect way to end the day. Take in the spectacular views of the colourful Ridgelands. Watch the sun go down across the desert horizon, while enjoying a hot beverage (tea, coffee, hot chocolate) in one hand and a home-made scone in the other.</p>
      <h3 class="subhead" style="font-size:8.5px">This tour includes</h3>
      <div class="rule"></div>
      <ul class="ticks ticks--rust">
        <li>The Boundary Fence</li>
        <li>The Lunar Flats</li>
        <li>The Ridgelands</li>
      </ul>
    </div>
    <div class="photo photo--ridges" role="img" aria-label="Colourful eroded desert ridges under a deep blue sky"></div>
    <svg class="wave" style="top:262px" width="187" height="40" viewBox="0 0 187 50" preserveAspectRatio="none" aria-hidden="true">
      <path d="M0 0 L187 0 L187 50 C150 10 90 30 40 14 C20 8 8 10 0 14 Z" fill="#ffffff"/>
      <path d="M0 14 C8 10 20 8 40 14 C90 30 150 10 187 50" fill="none" stroke="#d4552a" stroke-width="4"/>
    </svg>
  </article>
</section>

<section class="sheet sheet--outside" aria-label="Outside spread">

  <article class="panel panel--dark">
    <div class="text-block" style="top:22px">
      <h2 class="title"><span class="accent">Subsurface Gemhunt</span><br>(prospecting) Tour: $50</h2>
      <div class="rule"></div>
      <p class="meta">Duration approx. 2 hours</p>
      <p class="meta">9.30am start</p>
      <p class="body">This tour is ideal for those who don't mind getting down and dirty whilst searching for their own opals.</p>
      <p class="body">Exclusive to Kestrel Treks, this impressive opal mine has extracted hundreds of thousands of dollars worth of opal.</p>
      <p class="body">After a quick introduction to prospecting, you will be handed a blacklight, sieve and shovel to explore the tailings in the hopes of finding your own piece of opal to take home with you. A truly unique experience.</p>
    </div>
    <div class="photo photo--tunnel" role="img" aria-label="Tour guide shining a torch into an underground mine tunnel"></div>
    <svg class="wave" style="top:268px" width="187" height="40" viewBox="0 0 187 50" preserveAspectRatio="none" aria-hidden="true">
      <path d="M0 0 L187 0 L187 50 C150 12 80 30 30 10 C18 6 8 8 0 12 Z" fill="#2b2b2b"/>
      <path d="M0 12 C8 8 18 6 30 10 C80 30 150 12 187 50" fill="none" stroke="#d4552a" stroke-width="4"/>
    </svg>
  </article>

  <article class="panel panel--light contact">
    <h2 class="title">Visit us at</h2>
    <div class="rule"></div>
    <svg class="icon" width="16" height="16" viewBox="0 0 16 16" aria-hidden="true"><circle cx="8" cy="8" r="8" fill="#d4552a"/><rect x="5.5" y="3.5" width="5" height="9" rx="1" fill="none" stroke="#fff" stroke-width="1.2"/></svg>
    <p class="line">0488 217 654</p>
    <svg class="icon" width="16" height="16" viewBox="0 0 16 16" aria-hidden="true"><circle cx="8" cy="8" r="8" fill="#d4552a"/><rect x="4" y="5" width="8" height="6" fill="none" stroke="#fff" stroke-width="1.1"/><path d="M4 5 L8 8.5 L12 5" fill="none" stroke="#fff" stroke-width="1.1"/></svg>
    <p class="line" style="font-size:7.2px">kestreltreksoz@mailbox-example.net</p>
    <div class="booking-bar">Online bookings</div>
    <p class="line" style="font-size:7.2px">www.kestreltreksoz-example.com.au</p>
    <p class="body" style="font-size:7.6px">Tours can also be booked directly through the reception at the Harlow Ridge Desert Lodge and the Clay Nest Inn.</p>
    <div class="brand-row brand-row--inn"><span class="mark-square"></span>Clay Nest Inn</div>
    <div class="brand-row brand-row--lodge"><span class="mark-circle"></span>Harlow Ridge</div>
    <div class="partners"><span class="partner"></span><span class="partner partner--green"></span></div>
  </article>

  <article class="panel panel--dark">
    <div class="photo photo--glasses" role="img" aria-label="Two glasses of sparkling wine on a rocky lookout above the desert"></div>
    <svg class="wave" style="top:190px" width="187" height="60" viewBox="0 0 187 60" preserveAspectRatio="none" aria-hidden="true">
      <path d="M0 60 L0 40 C60 60 120 0 187 20 L187 60 Z" fill="#2b2b2b"/>
      <path d="M0 40 C60 60 120 0 187 20" fill="none" stroke="#d4552a" stroke-width="3"/>
    </svg>
    <div class="emblem"><span class="mark-square"></span>Kestrel Treks</div>
    <ul class="ticks ticks--rust front-list">
      <li>Grand Circuit of the Village and Ridgelands</li>
      <li>Opalvale Showcase Tour</li>
      <li>Twilight Ridgelands Tour</li>
      <li>Subsurface Gemhunt (prospecting) Tour.</li>
    </ul>
  </article>
</section>

</body>
</html>
```